Velmorastry

I need a poster design for an upcoming show. I'm a magician I have a picture I'd like to use as the basic format but I need verbiage and other border ideas and fonts

Target Market(s)

All ages

Industry/Entity Type

Entertainment Industry

Font styles to use
Sans Serif

Requirements
Must have
• On top of the poster I need VELMOR and at the bottom the word Magician. The names have to pop! I'm open to font ideas. A Border, all text regarding show time date ect.
• Brackenfell convention center
• Aug. 21st
• 8:30 pm
• 555-314-2768
• Brackenfellhub.example
• Also I'd like to have the tv appearances I've made on the poster off to the side wt in some kind of bubble/star/screen and inside that have the tv shows I've been on logos such as NATION'S STAR QUEST FINALIST, The Morvy show, QRZ, BXN, this is basically a lore for people to come to the show.
Nice to have
• A border, filigree
Should not have
• Top hat, rabbit

```html
<!DOCTYPE html>
<html lang="en">
<head>
<meta charset="utf-8">
<title>VELMOR – Illusionist</title>
<link rel="stylesheet" href="https://fonts.googleapis.com/css2?family=Anton&family=Antonio:wght@200;300&family=Questrial&display=swap">
<style>
  :root {
    --paper: #ffffff;
    --ink-light: #ffffff;
    --accent-cyan: #2bc4cf;
    --stage-dark: #1c1c1c;
    --stage-mid: #5a5a5a;
    --bubble-fill: rgba(20, 20, 20, 0.55);
  }
  html, body {
    margin: 0;
    padding: 0;
    overflow: hidden;
    background: var(--paper);
  }
  .poster {
    position: relative;
    width: 808px;
    height: 1200px;
    background: var(--paper);
    overflow: hidden;
  }
  .poster-border {
    position: absolute;
    left: 12px;
    top: 22px;
    width: 784px;
    height: 1164px;
    box-sizing: border-box;
    border: 2px solid var(--stage-dark);
  }
  .stage-photo {
    position: absolute;
    left: 24px;
    top: 36px;
    width: 756px;
    height: 1136px;
    background:
      radial-gradient(ellipse at 40% 60%, rgba(150, 150, 150, 0.55) 0%, rgba(60, 60, 60, 0.2) 45%, transparent 70%),
      linear-gradient(180deg, #3a3a3a 0%, var(--stage-dark) 40%, #2e2e2e 70%, var(--stage-mid) 100%);
  }
  .headline {
    position: absolute;
    left: 0;
    width: 808px;
    text-align: center;
    margin: 0;
    color: var(--ink-light);
  }
  .headline-name {
    top: 110px;
    font-family: "Anton", sans-serif;
    font-size: 228px;
    line-height: 1;
    letter-spacing: -2px;
    transform: scaleX(0.69);
    text-shadow: 14px 10px 0 var(--accent-cyan);
  }
  .headline-role {
    top: 358px;
    font-family: "Antonio", sans-serif;
    font-weight: 200;
    font-size: 84px;
    line-height: 1;
    letter-spacing: 12px;
    padding-left: 18px;
    text-shadow: 12px 10px 0 var(--accent-cyan);
  }
  .tv-bubble {
    position: absolute;
    left: 48px;
    top: 560px;
    width: 250px;
    height: 250px;
    box-sizing: border-box;
    border: 3px solid var(--ink-light);
    border-radius: 50%;
    background: var(--bubble-fill);
    color: var(--ink-light);
    font-family: "Questrial", sans-serif;
    text-align: center;
    display: flex;
    flex-direction: column;
    justify-content: center;
    align-items: center;
  }
  .tv-bubble p {
    margin: 0;
    line-height: 1.15;
    white-space: nowrap;
  }
  .tv-label {
    font-size: 14px;
    letter-spacing: 4px;
    color: var(--accent-cyan);
    margin-bottom: 10px !important;
  }
  .tv-credit {
    font-size: 17px;
    letter-spacing: 2px;
  }
  .tv-credit + .tv-credit {
    margin-top: 8px !important;
  }
  .tv-credit-lead {
    font-size: 15px;
    letter-spacing: 1px;
  }
  .headline-trade {
    position: absolute;
    left: 50px;
    top: 1046px;
    margin: 0;
    font-family: "Antonio", sans-serif;
    font-weight: 200;
    font-size: 70px;
    line-height: 1;
    letter-spacing: 6px;
    color: var(--ink-light);
    text-shadow: 8px 7px 0 var(--accent-cyan);
  }
  .show-details {
    position: absolute;
    left: 332px;
    top: 712px;
    width: 432px;
    height: 424px;
    box-sizing: border-box;
    border: 4px solid var(--ink-light);
    color: var(--ink-light);
    font-family: "Questrial", sans-serif;
    text-align: center;
  }
  .show-details p {
    margin: 0;
    line-height: 1;
    white-space: nowrap;
  }
  .venue-name {
    margin-top: 36px !important;
    font-size: 46px;
    letter-spacing: 5px;
  }
  .venue-type {
    margin-top: 8px !important;
    font-size: 24px;
    letter-spacing: 5px;
  }
  .show-date {
    margin-top: 28px !important;
    font-size: 76px;
    letter-spacing: 11px;
  }
  .show-time {
    margin-top: 22px !important;
    font-size: 76px;
    letter-spacing: 9px;
  }
  .contact-phone {
    margin-top: 20px !important;
    font-size: 42px;
    letter-spacing: 6px;
  }
  .contact-web {
    margin-top: 10px !important;
    font-size: 21px;
    letter-spacing: 3px;
  }
</style>
</head>
<body>
  <main class="poster">
    <div class="poster-border"></div>
    <div class="stage-photo" role="img" aria-label="Black and white stage photograph of an illusionist tipping a large box with red, violet and green panels while an assistant in a feathered costume poses behind him"></div>

    <h1 class="headline headline-name">VELMOR</h1>
    <p class="headline headline-role">ILLUSIONIST</p>

    <aside class="tv-bubble">
      <p class="tv-label">AS SEEN ON</p>
      <p class="tv-credit tv-credit-lead">NATION'S STAR QUEST</p>
      <p class="tv-credit tv-credit-lead">FINALIST</p>
      <p class="tv-credit">THE MORVY SHOW</p>
      <p class="tv-credit">QRZ &nbsp;·&nbsp; BXN</p>
    </aside>

    <p class="headline-trade">MAGICIAN</p>

    <section class="show-details">
      <p class="venue-name">BRACKENFELL</p>
      <p class="venue-type">CONVENTION CENTER</p>
      <p class="show-date">AUG 21</p>
      <p class="show-time">8:30 PM</p>
      <p class="contact-phone">555-314-2768</p>
      <p class="contact-web">BRACKENFELLHUB.EXAMPLE</p>
    </section>
  </main>
</body>
</html>
```